Lantern Hill Publicity is a new boutique Press Office with a small roster of well-chosen clients across an array of disciplines; from Art and Technology to Restaurants and Fashion. Based in Greenpoint Brooklyn, Lantern Hill Publicity achieves outstanding results through hard work, tenacity, efficiency and a sense of humor. We need a simple, versatile and classic design. We would like each side of the card to be white text on a black background.

Boutique

```html
<!DOCTYPE html>
<html lang="en">
<head>
<meta charset="utf-8">
<title>Lantern Hill Publicity — Business Card</title>
<link rel="stylesheet" href="https://fonts.googleapis.com/css2?family=Cinzel:wght@400;700&family=Lato:wght@400&display=swap">
<style>
  :root {
    --backdrop: #bdbdbd;
    --card: #000000;
    --ink: #ffffff;
    --ink-soft: #e6e6e6;
  }
  * { margin: 0; padding: 0; box-sizing: border-box; }
  html, body {
    width: 1200px;
    height: 837px;
    overflow: hidden;
    background: var(--backdrop);
  }
  .canvas {
    position: relative;
    width: 1200px;
    height: 837px;
  }
  .card {
    position: absolute;
    top: 270px;
    width: 520px;
    height: 297px;
    background: var(--card);
    color: var(--ink);
    box-shadow: 0 6px 18px rgba(0,0,0,0.25);
  }
  .card--front { left: 60px; }
  .card--back { left: 620px; }

  .wordmark {
    font-family: "Cinzel", serif;
    font-weight: 400;
    color: var(--ink);
    text-align: center;
  }
  .wordmark__name {
    display: block;
    font-size: 30px;
    letter-spacing: 0.16em;
    line-height: 1;
  }
  .wordmark__line {
    display: block;
    font-size: 11px;
    letter-spacing: 0.7em;
    margin-top: 8px;
    padding-left: 0.7em;
  }
  .card--front .wordmark {
    position: absolute;
    left: 0; right: 0;
    top: 50%;
    transform: translateY(-50%);
  }
  .card--back .wordmark {
    position: absolute;
    left: 36px;
    top: 44px;
    text-align: left;
  }
  .card--back .wordmark__name { font-size: 24px; }
  .card--back .wordmark__line { font-size: 9px; padding-left: 0; }

  .contact {
    position: absolute;
    right: 34px;
    bottom: 32px;
    font-family: "Lato", sans-serif;
    font-size: 12px;
    line-height: 1.5;
    color: var(--ink-soft);
  }
  .contact__name {
    font-family: "Cinzel", serif;
    font-weight: 700;
    font-size: 15px;
    letter-spacing: 0.04em;
    color: var(--ink);
    line-height: 1.2;
  }
  .contact__role { margin-bottom: 8px; }
  .contact__label {
    font-family: "Cinzel", serif;
    font-weight: 700;
    color: var(--ink);
    display: inline-block;
    width: 18px;
  }
</style>
</head>
<body>
<main class="canvas">
  <section class="card card--front" aria-label="Card front">
    <div class="wordmark">
      <span class="wordmark__name">LANTERN HILL</span>
      <span class="wordmark__line">PUBLICITY</span>
    </div>
  </section>

  <section class="card card--back" aria-label="Card back">
    <div class="wordmark">
      <span class="wordmark__name">LANTERN HILL</span>
      <span class="wordmark__line">PUBLICITY</span>
    </div>
    <div class="contact">
      <p class="contact__name">MARA ELLISON</p>
      <p class="contact__role">Chief Executive Officer</p>
      <p><span class="contact__label">P:</span>718 555 0142</p>
      <p><span class="contact__label">E:</span>mara@lanternhillpr.com</p>
      <p><span class="contact__label">W:</span>www.lanternhillpr.com</p>
    </div>
  </section>
</main>
</body>
</html>
```